Business card design for new eCommerce site focusing on integrity and strong businsess tactics

We need a business card that will stand out and be memorable. Something with color that matches our company logo colors. Think high end version of Dealvine. There are 2 logos provided. The parent company is called Bright Harbor Ventures and we are presenting a new and very exciting eCommerce site called KeenTraders.example.

Target Market(s)

Our target markets are in the Activities, Food and Beverage, Health and Beauty

Industry/Entity Type

Marketing

Contact Information for Business Card

We have 4 members that need cards...I will provide all info to the winner of the design contest
Business Address is
48730 West 61st Avenue, Suite C204
Phoenix AZ 85917

Font styles to use
Serif
Sans Serif

Colors

Designer to choose colors to be used in the design.

Requirements
Must have
• The card must be memorable...should be unique in design but must exude integrity and be playful .
• I have provided several colors or our parent company...please feel free to use which ever
Nice to have
• I will leave this up to you. Feel free to use other images of your choosing that wraps around our client.....Activities, Dining, Health, Beauty
Should not have
• just dont be boring

```html
<!DOCTYPE html>
<html lang="en">
<head>
<meta charset="utf-8">
<title>KeenTraders.example Business Card</title>
<link rel="stylesheet" href="https://fonts.googleapis.com/css2?family=Mulish:wght@400;600;800&display=swap">
<style>
  :root {
    --bg: #2b2b2b;
    --blue-light: #3fb6dc;
    --blue: #2d86c0;
    --blue-deep: #1f6fa8;
    --green: #7dc233;
    --green-light: #b3df55;
    --white: #ffffff;
    --paper: #f1f1f1;
    --text-grey: #555c63;
  }
  * { margin: 0; padding: 0; box-sizing: border-box; }
  html, body {
    width: 1042px; height: 1200px; overflow: hidden;
    background: var(--bg);
    font-family: "Mulish", sans-serif;
  }
  .canvas { position: relative; width: 1042px; height: 1200px; }
  .card {
    position: absolute; left: 129px; width: 787px; height: 449px;
    border-radius: 24px; overflow: hidden;
  }
  .card-front { top: 100px; background: var(--paper); }
  .card-back {
    top: 633px;
    background: linear-gradient(135deg, var(--green-light) 0%, var(--green) 40%, var(--green) 100%);
    color: var(--white); text-align: center;
  }
  .front-art { position: absolute; inset: 0; }
  .contact { position: absolute; left: 37px; top: 0; color: var(--white); }
  .contact-name {
    position: absolute; top: 94px; white-space: nowrap;
    font-size: 29px; font-weight: 800; color: var(--green-light); letter-spacing: 0.5px;
  }
  .contact-role { position: absolute; top: 130px; white-space: nowrap; font-size: 18px; }
  .contact-address { position: absolute; top: 174px; white-space: nowrap; font-size: 18px; line-height: 24px; }
  .contact-list { position: absolute; top: 254px; list-style: none; font-size: 18px; line-height: 25px; }
  .contact-list li { display: flex; align-items: center; white-space: nowrap; }
  .contact-list svg { width: 16px; height: 16px; margin-right: 13px; flex: none; }
  .brand-front { position: absolute; left: 425px; top: 193px; }
  .brand-name { font-size: 33px; font-weight: 600; color: var(--blue); letter-spacing: -0.5px; white-space: nowrap; }
  .brand-tagline { font-size: 15px; color: var(--text-grey); letter-spacing: 2px; white-space: nowrap; margin-top: 2px; }
  .brand-back { position: absolute; left: 0; right: 0; top: 168px; }
  .brand-back .brand-name { color: var(--white); font-size: 48px; }
  .brand-back .brand-tagline { color: var(--white); font-size: 22px; letter-spacing: 4.5px; margin-top: 4px; }
  .slogan {
    position: absolute; left: 0; right: 0; top: 367px;
    display: flex; align-items: center; justify-content: center;
    font-size: 18px; font-weight: 800; letter-spacing: 0.5px;
  }
  .slogan::before, .slogan::after {
    content: ""; width: 115px; height: 2px; margin: 0 4px;
  }
  .slogan::before { background: linear-gradient(90deg, transparent, var(--white)); }
  .slogan::after { background: linear-gradient(90deg, var(--white), transparent); }
</style>
</head>
<body>
<main class="canvas">
  <section class="card card-front" aria-label="Card front">
    <svg class="front-art" viewBox="0 0 787 449" aria-hidden="true">
      <defs>
        <linearGradient id="panelBlue" x1="0" y1="0" x2="1" y2="1">
          <stop offset="0" stop-color="var(--blue-light)"/>
          <stop offset="0.55" stop-color="var(--blue)"/>
          <stop offset="1" stop-color="var(--blue-deep)"/>
        </linearGradient>
      </defs>
      <path d="M0 0 H400 C330 90 300 230 405 449 H0 Z" fill="url(#panelBlue)"/>
      <path d="M400 0 C330 90 300 230 405 449" fill="none" stroke="var(--white)" stroke-width="14"/>
      <path d="M416 0 C350 95 325 240 420 449" fill="none" stroke="var(--blue)" stroke-width="7"/>
      <path d="M410 6 C365 40 348 95 380 155 C360 100 370 50 410 6 Z" fill="var(--green)"/>
      <path d="M368 225 C375 300 400 370 395 430 C418 370 405 290 368 225 Z" fill="var(--green)"/>
    </svg>

    <div class="contact">
      <h1 class="contact-name">MARA QUILL</h1>
      <p class="contact-role">SUBSCRIPTION SALES</p>
      <address class="contact-address" style="font-style:normal">
        48730 West 61st Avenue<br>Suite C204<br>Phoenix AZ 85917
      </address>
      <ul class="contact-list">
        <li><svg viewBox="0 0 16 16"><path d="M3 1l3 3-2 2c1 2 3 4 5 5l2-2 3 3-2 3C7 15 1 9 1 3z" fill="var(--green)"/></svg>602-555-0187</li>
        <li><svg viewBox="0 0 16 16"><rect x="4" y="1" width="8" height="14" rx="1.5" fill="none" stroke="var(--green)" stroke-width="1.8"/><rect x="7" y="12" width="2" height="1.5" fill="var(--green)"/></svg>602 555 0142</li>
        <li><svg viewBox="0 0 16 16"><rect x="1" y="3" width="14" height="10" fill="var(--green)"/><path d="M1 3l7 6 7-6" fill="none" stroke="var(--blue)" stroke-width="1.2"/></svg>Mara@KeenTraders.example</li>
        <li><svg viewBox="0 0 16 16"><circle cx="8" cy="8" r="7" fill="var(--green)"/><path d="M1 8h14M8 1c-3 4-3 10 0 14M8 1c3 4 3 10 0 14" fill="none" stroke="var(--blue)" stroke-width="1"/></svg>www.KeenTraders.example</li>
      </ul>
    </div>

    <div class="brand-front">
      <p class="brand-name">KeenTraders.example</p>
      <p class="brand-tagline">Activities-Dining-Health-Beauty</p>
    </div>
  </section>

  <section class="card card-back" aria-label="Card back">
    <div class="brand-back">
      <p class="brand-name">KeenTraders.example</p>
      <p class="brand-tagline">Activities-Dining-Health-Beauty</p>
    </div>
    <p class="slogan">LOOKING OUT FOR YOU</p>
  </section>
</main>
</body>
</html>
```